CareStatute Chambers Mailer for Small Medical Offices and Solo Physician Practices

CareStatute Chambers -- We are a local health law firm looking to provide advice to medical practices on the legal issues they face. We strive to function as a general counsel for medical practices and provide tailored solutions to meet the needs of our clients. Please see postcard content ideas in document attached. Our firm colors are royal blue, gray and white and black.

Target Market(s)

Small medical offices, solo physician practices in the Southeast Michigan (Detroit Metro area)

Industry/Entity Type

Law Firm

Font styles to use
Sans Serif

Colors
0991cd
3176b5
ffffff
7f7f7f
1b1b1b

Requirements
Must have
• Brief summary of legal services offered, bullet pointed list of practice areas/issues
• Contact information, website, address
• Pictures of attorneys
• Prefer the use of our firm's colors (royal blue, gray, white, black)
Nice to have
• Included some purchased stock images that could also be incorporated

```html
<!DOCTYPE html>
<html lang="en">
<head>
<meta charset="utf-8">
<title>CareStatute Chambers Mailer</title>
<link href="https://fonts.googleapis.com/css2?family=Arimo:wght@400;700&family=Lato:wght@400;700&display=swap" rel="stylesheet">
<style>
  :root {
    --blue: #0991cd;
    --royal: #3176b5;
    --white: #ffffff;
    --gray: #7f7f7f;
    --ink: #1b1b1b;
    --panel: #f4f5f7;
    --band: #1c8fd0;
    --back-blue: #2a93d3;
    --canvas: #e6e7e9;
  }
  * { margin: 0; padding: 0; box-sizing: border-box; }
  html, body { width: 1200px; height: 1200px; overflow: hidden; }
  body { background: var(--canvas); font-family: "Arimo", Arial, sans-serif; color: var(--ink); position: relative; }

  .card { position: absolute; left: 172px; width: 886px; height: 492px; background: var(--white); box-shadow: 0 4px 14px rgba(0,0,0,.25); overflow: hidden; }
  .card--front { top: 94px; }
  .card--back { top: 640px; }
  .card__art { position: absolute; inset: 0; width: 100%; height: 100%; }
  .abs { position: absolute; }

  .brand { left: 26px; top: 222px; width: 315px; height: 70px; background: var(--white); display: flex; align-items: center; gap: 12px; padding-left: 12px; }
  .brand__name { font-family: "Arimo", sans-serif; font-weight: 700; font-size: 25px; color: var(--royal); white-space: nowrap; }
  .brand__mark { width: 14px; height: 14px; background: var(--gray); }

  .headline { left: 26px; top: 316px; font-size: 31px; font-weight: 700; color: var(--royal); letter-spacing: .3px; }

  .intro { left: 27px; top: 377px; width: 560px; color: var(--white); }
  .intro__title { font-size: 16px; font-weight: 700; margin-bottom: 4px; }
  .intro__text { font-family: "Lato", sans-serif; font-size: 10px; line-height: 13px; }

  .contact { left: 656px; top: 342px; width: 220px; font-size: 12px; line-height: 14.5px; color: var(--ink); }
  .contact__title { font-weight: 700; font-size: 13px; margin-bottom: 4px; margin-left: 16px; }
  .contact__row { display: flex; gap: 8px; align-items: flex-start; margin-bottom: 5px; }
  .contact__row svg { flex: none; margin-top: 1px; }

  .back__intro { left: 27px; top: 34px; width: 440px; font-size: 12px; line-height: 14.5px; }
  .practice { left: 18px; top: 108px; display: grid; grid-template-columns: 226px 250px; row-gap: 9px; color: var(--white); font-size: 13px; }
  .practice li { list-style: none; white-space: nowrap; }
  .practice li::before { content: "- "; }
  .back__service { left: 27px; top: 245px; width: 460px; color: var(--white); font-size: 12px; line-height: 14.5px; }

  .attorney__name { font-family: "Lato", sans-serif; font-size: 10px; font-weight: 700; color: var(--blue); line-height: 13px; }
  .attorney__role { font-family: "Lato", sans-serif; font-size: 10px; color: var(--gray); line-height: 13px; }

  .footer { left: 0; top: 420px; width: 494px; height: 72px; background: var(--gray); color: var(--white); font-size: 10.5px; line-height: 13px; display: flex; align-items: center; gap: 14px; padding-left: 12px; }
  .footer__item { display: flex; gap: 6px; align-items: center; white-space: nowrap; }

  .mail-brand { left: 512px; top: 38px; display: flex; align-items: center; gap: 8px; }
  .mail-brand .brand__name { font-size: 15px; }
  .mail-brand .brand__mark { width: 9px; height: 9px; }
  .stamp { left: 802px; top: 37px; width: 54px; height: 70px; border: 1px solid var(--gray); }
  .web { left: 521px; top: 432px; font-size: 14.5px; letter-spacing: 3.6px; color: var(--ink); }
</style>
</head>
<body>

<section class="card card--front">
  <svg class="card__art" viewBox="0 0 886 492" aria-hidden="false">
    <defs>
      <linearGradient id="photoTone" x1="0" y1="0" x2="1" y2="1">
        <stop offset="0" stop-color="#e9eef5"/>
        <stop offset=".45" stop-color="#5b79b8"/>
        <stop offset=".75" stop-color="#6b2a26"/>
        <stop offset="1" stop-color="#24408a"/>
      </linearGradient>
    </defs>
    <g role="img" aria-label="Stock photo of a wooden judge's gavel beside a stethoscope on a blue book">
      <rect x="0" y="0" width="886" height="380" fill="url(#photoTone)"/>
    </g>
    <path d="M0 198 L350 198 C400 198 415 235 432 285 C452 345 478 358 540 358 L640 358 C690 358 690 300 740 300 L886 300 L886 492 L0 492 Z" fill="var(--panel)" stroke="#777" stroke-width="4"/>
    <path d="M0 370 L625 370 C600 395 590 462 520 462 L0 462 Z" fill="var(--band)" stroke="#777" stroke-width="3"/>
  </svg>

  <div class="abs brand"><span class="brand__name">CareStatute Chambers</span><span class="brand__mark"></span></div>
  <h1 class="abs headline">HEALTH LAW QUESTIONS?</h1>

  <div class="abs intro">
    <h2 class="intro__title">CareStatute Chambers</h2>
    <p class="intro__text">We are a local health law firm looking to provide advice to medical practices on the legal issues they face. We strive to function as a general counsel for medical practices and provide tailored solutions to meet the needs of our clients. Please see postcard content in document attached. Our firm colors are royal blue, gray, white and black.</p>
  </div>

  <div class="abs contact">
    <p class="contact__title">Free consultations available:</p>
    <div class="contact__row">
      <svg width="12" height="15" viewBox="0 0 12 15"><path d="M6 0a6 6 0 0 0-6 6c0 4 6 9 6 9s6-5 6-9a6 6 0 0 0-6-6z" fill="var(--blue)"/><circle cx="6" cy="6" r="2.2" fill="#fff"/></svg>
      <span>CareStatute Chambers<br>4180 Lakeshore Drive, Suite 310<br>Farmbrook, MI 48091</span>
    </div>
    <div class="contact__row">
      <svg width="15" height="15" viewBox="0 0 15 15"><circle cx="7.5" cy="7.5" r="6.8" fill="none" stroke="var(--blue)" stroke-width="1.2"/><path d="M5 4l1.5 1.6-.8 1.2c.5 1 1.3 1.8 2.3 2.3l1.2-.8L10.8 10l-1 1.2C7 11 4.2 8 4 5z" fill="var(--blue)"/></svg>
      <span>248.555.0174</span>
    </div>
    <div class="contact__row">
      <svg width="15" height="12" viewBox="0 0 15 12"><rect x=".6" y=".6" width="13.8" height="10.8" fill="none" stroke="var(--blue)" stroke-width="1.2"/><path d="M.6.6 7.5 7 14.4.6M.6 11.4 5.5 5.5M14.4 11.4 9.5 5.5" fill="none" stroke="var(--blue)" stroke-width="1.2"/></svg>
      <span>info@carestatutechambers.com</span>
    </div>
    <div class="contact__row">
      <svg width="15" height="15" viewBox="0 0 15 15" fill="none" stroke="var(--blue)" stroke-width="1"><circle cx="7.5" cy="7.5" r="6.8"/><ellipse cx="7.5" cy="7.5" rx="3" ry="6.8"/><path d="M.7 7.5h13.6M2 4h11M2 11h11"/></svg>
      <span>www.carestatutechambers.com</span>
    </div>
  </div>
</section>

<section class="card card--back">
  <svg class="card__art" viewBox="0 0 886 492">
    <rect x="0" y="0" width="494" height="420" fill="var(--panel)"/>
    <path d="M0 82 L70 82 L82 98 L94 82 L494 82 L494 346 L0 346 Z" fill="var(--back-blue)"/>
    <g role="img" aria-label="Portrait photo of partner Maren Delacroix">
      <circle cx="68" cy="354" r="56" fill="#6d6a6c" stroke="#d9dadc" stroke-width="4"/>
    </g>
    <g role="img" aria-label="Portrait photo of partner Lydia Brandt">
      <circle cx="322" cy="354" r="56" fill="#8a8580" stroke="#d9dadc" stroke-width="4"/>
    </g>
  </svg>

  <p class="abs back__intro">We are local, experienced health lawyers available to provide efficient, effective advice on the issues impacting your healthcare business every day, including:</p>

  <ul class="abs practice">
    <li>Contract review and negotiation</li><li>Licensing matters</li>
    <li>Stark and Anti-kickback matters</li><li>Employee issues</li>
    <li>Reimbursement and payer issues</li><li>Difficult patient matters</li>
    <li>HIPAA</li><li>Subpoenas and medical record requests</li>
    <li>Vendor issues</li><li>Leases and landlord-tenant issues</li>
  </ul>

  <p class="abs back__service">We provide personalized service to our clients so you have trusted counsel available when you need it. We offer competitive hourly rates as well as flat fee arrangements when possible.</p>

  <div class="abs" style="left:133px;top:362px"><p class="attorney__name">MAREN DELACROIX,</p><p class="attorney__role">Partner</p></div>
  <div class="abs" style="left:386px;top:362px"><p class="attorney__name">LYDIA BRANDT,</p><p class="attorney__role">Partner</p></div>

  <div class="abs footer">
    <div class="footer__item">
      <svg width="12" height="15" viewBox="0 0 12 15"><path d="M6 0a6 6 0 0 0-6 6c0 4 6 9 6 9s6-5 6-9a6 6 0 0 0-6-6z" fill="#fff"/><circle cx="6" cy="6" r="2.2" fill="var(--gray)"/></svg>
      <span>4180 Lakeshore Drive, Suite 310<br>Farmbrook, MI 48091</span>
    </div>
    <div class="footer__item">
      <svg width="15" height="15" viewBox="0 0 15 15"><circle cx="7.5" cy="7.5" r="6.8" fill="none" stroke="#fff" stroke-width="1.2"/><path d="M5 4l1.5 1.6-.8 1.2c.5 1 1.3 1.8 2.3 2.3l1.2-.8L10.8 10l-1 1.2C7 11 4.2 8 4 5z" fill="#fff"/></svg>
      <span>248.555.0174</span>
    </div>
    <div class="footer__item">
      <svg width="15" height="12" viewBox="0 0 15 12"><rect x=".6" y=".6" width="13.8" height="10.8" fill="none" stroke="#fff" stroke-width="1.2"/><path d="M.6.6 7.5 7 14.4.6M.6 11.4 5.5 5.5M14.4 11.4 9.5 5.5" fill="none" stroke="#fff" stroke-width="1.2"/></svg>
      <span>info@carestatutechambers.com</span>
    </div>
  </div>

  <div class="abs mail-brand"><span class="brand__name">CareStatute Chambers</span><span class="brand__mark"></span></div>
  <div class="abs stamp"></div>
  <p class="abs web">www.carestatutechambers.com</p>
</section>

</body>
</html>
```